Refrigeration & Air Conditioning modern and appealing

We want to design a business card that is modern and appealing using existing logo supplied

Front card
Residential Commercial Diary
RTA : AU071523
Licence L258907

Back card
Marcus Ovenly
Director
0491 352 406
info@frostvalecooling.com.au
www.frostvalecooling.com.au
• Air Conditioning
• Cool Rooms & Refrigeration
• Installation
• Service & Repair
• Preventative Maintenance

We offer 24/7 emergency service

```html
<!DOCTYPE html>
<html lang="en">
<head>
<meta charset="utf-8">
<title>Frostvale Cooling – Business Card</title>
<link href="https://fonts.googleapis.com/css2?family=Montserrat:wght@400;500;700;800&display=swap" rel="stylesheet">
<style>
  :root {
    --backdrop: #3b3b3d;
    --card: #151516;
    --white: #f4f4f6;
    --silver: #c9c9cc;
    --muted: #d8d8dc;
    --purple: #b08ad6;
    --purple-deep: #8a55c2;
  }
  * { margin: 0; padding: 0; box-sizing: border-box; }
  html, body {
    width: 1200px; height: 689px; overflow: hidden;
    background: var(--backdrop);
    font-family: "Montserrat", sans-serif;
  }
  .stage { position: relative; width: 1200px; height: 689px; }
  .card {
    position: absolute; top: 190px;
    width: 540px; height: 309px;
    background: var(--card);
    border-radius: 18px;
    box-shadow: 0 20px 40px rgba(0,0,0,.45);
    color: var(--white);
  }
  .card--front { left: 40px; }
  .card--back { left: 620px; }

  .brand {
    display: flex; align-items: center; gap: 12px;
    font-weight: 800; letter-spacing: 2px;
    white-space: nowrap; line-height: 1;
  }
  .brand__dot { width: 22px; height: 22px; border-radius: 50%; flex: none; }

  /* front */
  .card--front .brand {
    position: absolute; left: 56px; top: 100px;
    font-size: 30px; color: var(--silver);
  }
  .card--front .brand__dot { background: var(--silver); }
  .credentials {
    position: absolute; right: 56px; top: 168px;
    text-align: center; font-size: 12.5px; line-height: 1.5;
    color: var(--muted); font-weight: 400;
  }

  /* back */
  .card--back .brand {
    position: absolute; left: 30px; top: 42px;
    font-size: 22px; color: var(--white);
  }
  .card--back .brand__dot { background: var(--purple); width: 18px; height: 18px; }
  .emergency {
    position: absolute; right: 28px; top: 90px;
    font-size: 13px; color: var(--white); white-space: nowrap;
  }
  .services {
    position: absolute; right: 28px; top: 118px;
    list-style: none; text-align: right;
    font-size: 11.5px; line-height: 1.5; color: var(--white);
    white-space: nowrap;
  }
  .person {
    position: absolute; left: 30px; top: 150px;
    padding-left: 16px;
    border-left: 6px solid var(--purple-deep);
  }
  .person__name { font-size: 25px; font-weight: 700; color: var(--purple); line-height: 1.1; white-space: nowrap; }
  .person__role { font-size: 14px; color: var(--white); margin-top: 2px; }
  .contacts {
    position: absolute; left: 52px; top: 228px;
    list-style: none; font-size: 11.5px; line-height: 1.6; color: var(--white);
  }
  .contacts li { display: flex; align-items: center; gap: 7px; white-space: nowrap; }
  .contacts svg { width: 11px; height: 11px; fill: var(--purple); flex: none; }
</style>
</head>
<body>
<div class="stage">

  <section class="card card--front">
    <div class="brand"><span class="brand__dot"></span>FROSTVALE COOLING</div>
    <p class="credentials">
      Residential Commercial Diary<br>
      RTA : AU071523<br>
      Licence L258907
    </p>
  </section>

  <section class="card card--back">
    <div class="brand"><span class="brand__dot"></span>FROSTVALE COOLING</div>
    <p class="emergency">We offer 24/7 emergency service</p>
    <ul class="services">
      <li>Air Conditioning</li>
      <li>Cool Rooms &amp; Refrigeration</li>
      <li>Installation</li>
      <li>Service &amp; Repair</li>
      <li>Preventative Maintenance</li>
    </ul>

    <div class="person">
      <p class="person__name">Marcus Ovenly</p>
      <p class="person__role">Director</p>
    </div>

    <ul class="contacts">
      <li>
        <svg viewBox="0 0 24 24" aria-hidden="true"><path d="M6.6 10.8a15 15 0 0 0 6.6 6.6l2.2-2.2a1 1 0 0 1 1-.25 11.4 11.4 0 0 0 3.6.6 1 1 0 0 1 1 1V20a1 1 0 0 1-1 1A17 17 0 0 1 3 4a1 1 0 0 1 1-1h3.5a1 1 0 0 1 1 1c0 1.25.2 2.45.6 3.6a1 1 0 0 1-.25 1z"/></svg>
        0491 352 406
      </li>
      <li>
        <svg viewBox="0 0 24 24" aria-hidden="true"><path d="M2 5h20v14H2z M2 5l10 8 10-8" /></svg>
        info@frostvalecooling.com.au
      </li>
      <li>
        <svg viewBox="0 0 24 24" aria-hidden="true"><circle cx="12" cy="12" r="10"/></svg>
        www.frostvalecooling.com.au
      </li>
    </ul>
  </section>

</div>
</body>
</html>
```